New Webpage for High Class Expert Witness Services Company

We are looking for a minimalist design for a webpage that just has our logo and an entry form offer to connect with one of our Liaisons.
The entry form should just ask for Name, Email, Contact Info and Description of Project.

Company Name is: The Marlow Crest Advisory Services

Number of Pages Required

1 page

```html
<!DOCTYPE html>
<html lang="en">
<head>
<meta charset="utf-8">
<title>The Marlow Crest Advisory Services — Connect With a Liaison</title>
<link rel="stylesheet" href="https://fonts.googleapis.com/css2?family=Cinzel:wght@500;600;700&family=Inter:wght@400;500&display=swap">
<style>
  :root {
    --page-bg: #000000;
    --card-bg: #171717;
    --field-bg: #1d1d1d;
    --field-line: #4a4a4a;
    --text: #ffffff;
    --muted: #d8d8d8;
    --rule: #2c2c2c;
    --menu-bg: #2a2a2a;
    --silver-light: #ececee;
    --silver-dark: #8d8e92;
    --bracket: #e6e6e6;
    --button-text: #111111;
  }
  * { box-sizing: border-box; margin: 0; padding: 0; }
  html, body {
    width: 1200px; height: 639px; overflow: hidden;
    background: var(--page-bg); color: var(--text);
    font-family: "Inter", Arial, sans-serif;
  }
  .site-header {
    position: absolute; left: 0; top: 0; width: 1200px; height: 69px;
    border-bottom: 1px solid var(--rule);
  }
  .brand {
    position: absolute; left: 483px; top: 13px; width: 234px; height: 43px;
    display: flex; align-items: center; gap: 8px;
    font-family: "Cinzel", Georgia, serif; font-weight: 600;
    color: var(--text);
  }
  .brand-mark { width: 22px; height: 22px; background: var(--muted); flex: none; }
  .brand-name { font-size: 12px; line-height: 1.2; letter-spacing: 0.06em; text-transform: uppercase; }
  .menu-toggle {
    position: absolute; left: 939px; top: 19px; width: 53px; height: 31px;
    background: var(--menu-bg); border: 0;
  }
  .menu-toggle span { position: absolute; height: 1px; background: var(--text); }
  .menu-toggle span:nth-child(1) { left: 20px; top: 12px; width: 14px; }
  .menu-toggle span:nth-child(2) { left: 16px; top: 17px; width: 21px; }

  .contact-card {
    position: absolute; left: 208px; top: 132px; width: 784px; height: 444px;
    background: var(--card-bg);
  }
  .corner { position: absolute; width: 8px; height: 8px; border-color: var(--bracket); border-style: solid; border-width: 0; }
  .corner.tl { left: 0; top: 0; border-top-width: 1px; border-left-width: 1px; }
  .corner.tr { right: 0; top: 0; border-top-width: 1px; border-right-width: 1px; }
  .corner.bl { left: 0; bottom: 0; border-bottom-width: 1px; border-left-width: 1px; }
  .corner.br { right: 0; bottom: 0; border-bottom-width: 1px; border-right-width: 1px; }

  .card-title {
    position: absolute; left: 0; top: 42px; width: 100%; text-align: center;
    font-family: "Cinzel", Georgia, serif; font-weight: 600; font-size: 24px;
    line-height: 32px; letter-spacing: -0.02em;
  }
  .card-intro {
    position: absolute; left: 0; top: 82px; width: 100%; text-align: center;
    font-size: 10px; line-height: 14px; color: var(--text);
  }
  .liaison-form { position: absolute; left: 115px; top: 115px; width: 554px; height: 300px; }
  .field {
    display: block; width: 554px; height: 37px; margin-bottom: 10px;
    background: var(--field-bg); border: 0; border-bottom: 1px solid var(--field-line);
    padding: 0 19px; color: var(--text);
    font-family: "Inter", Arial, sans-serif; font-size: 10px;
  }
  .field::placeholder { color: var(--muted); }
  .field-description { height: 81px; padding-top: 14px; resize: none; margin-bottom: 0; }
  .form-actions {
    position: absolute; left: 178px; top: 247px;
    display: flex; gap: 2px;
  }
  .submit-btn {
    width: 160px; height: 37px; border: 0;
    background: linear-gradient(90deg, var(--silver-light), var(--silver-dark));
    font-family: "Cinzel", Georgia, serif; font-weight: 700; font-size: 10px;
    color: var(--button-text);
  }
  .submit-arrow { position: relative; width: 36px; height: 37px; }
  .submit-arrow svg { position: absolute; left: 13px; top: 13px; }
</style>
</head>
<body>
  <header class="site-header">
    <div class="brand">
      <span class="brand-mark"></span>
      <span class="brand-name">The Marlow Crest<br>Advisory Services</span>
    </div>
    <button class="menu-toggle" aria-label="Open menu"><span></span><span></span></button>
  </header>

  <main class="contact-card">
    <span class="corner tl"></span><span class="corner tr"></span>
    <span class="corner bl"></span><span class="corner br"></span>
    <h1 class="card-title">CONNECT WITH A LIAISON</h1>
    <p class="card-intro">Tell Us About Your Project &amp; Our Team Will Reach Out To You Shortly.</p>
    <form class="liaison-form">
      <input class="field" type="text" placeholder="Enter Your Name*">
      <input class="field" type="email" placeholder="Your Email Address*">
      <input class="field" type="tel" placeholder="Phone Number*">
      <textarea class="field field-description" placeholder="Description of Project*"></textarea>
      <div class="form-actions">
        <button class="submit-btn" type="submit">SUBMIT REQUEST</button>
        <span class="submit-arrow">
          <span class="corner tl"></span><span class="corner tr"></span>
          <span class="corner bl"></span><span class="corner br"></span>
          <svg width="10" height="10" viewBox="0 0 10 10" aria-hidden="true">
            <path d="M2 8 L8 2 M3.5 2 H8 V6.5" stroke="#fff" stroke-width="1.4" fill="none"/>
          </svg>
        </span>
      </div>
    </form>
  </main>
</body>
</html>
```